Business Card Design Project

Industry/Entity Type

Business

Contact Information for Business Card

The Mercy Hill Gospel Choir
Dean Farrow, Minister of Music

The Harvest Covenant Church of Greenfield
Founded 1792

Blinkr @themhgc
Picturo mercyhillgc
Friendwall friendwall.example/mhgc408
Website: mercyhillgc.example
For Bookings: (555) 552-MHGC
4827 Marlowe Avenue, Philadelphia, PA 19144

Back of the Card
Music and Cd's Recordings Available On
Choirs Website and Also
Tunevault, Orbita Music, Disc Pony (the music online logo)

```html
<!DOCTYPE html>
<html lang="en">
<head>
<meta charset="utf-8">
<title>The Mercy Hill Gospel Choir – Business Card</title>
<link rel="stylesheet" href="https://fonts.googleapis.com/css2?family=Josefin+Sans:wght@400;600&display=swap">
<style>
  :root {
    --ink: #000000;
    --paper: #ffffff;
    --page: #ffffff;
    --shadow: rgba(0, 0, 0, 0.55);
  }
  * { margin: 0; padding: 0; box-sizing: border-box; }
  html, body {
    width: 1200px; height: 1000px; overflow: hidden;
    background: var(--page);
    font-family: "Josefin Sans", "Futura", sans-serif;
    color: var(--ink);
  }
  .canvas { position: relative; width: 1200px; height: 1000px; }
  .card {
    position: absolute; left: 350px; width: 500px; height: 300px;
    background: var(--paper);
    box-shadow: 6px 6px 9px var(--shadow);
    overflow: hidden;
  }
  .card--front { top: 172px; }
  .card--back { top: 528px; }

  .front-band {
    position: absolute; left: 0; top: 0; width: 100%; height: 114px;
    background: var(--ink); color: var(--paper); text-align: center;
  }
  .choir-name {
    position: absolute; left: 0; right: 0; top: 50px;
    font-size: 24.5px; font-weight: 400; letter-spacing: -0.4px; text-transform: uppercase;
    white-space: nowrap;
  }
  .church-line {
    position: absolute; left: 0; right: 0; top: 87px;
    font-size: 11.5px; letter-spacing: -0.2px; white-space: nowrap;
  }

  .contact-block { position: absolute; left: 184px; top: 161px; right: 0; }
  .person {
    font-size: 15.5px; text-transform: uppercase; letter-spacing: -0.3px;
    padding-bottom: 2px; border-bottom: 2px solid var(--ink); white-space: nowrap;
  }
  .person-role { font-size: 10px; }
  .contact-grid {
    display: grid; grid-template-columns: 126px 1fr;
    row-gap: 6px; margin-top: 9px; font-size: 9.5px; line-height: 12px;
    white-space: nowrap;
  }
  .social { display: flex; align-items: center; gap: 4px; }
  .social-mark { width: 9px; height: 9px; flex: none; }

  .back-message {
    position: absolute; left: 0; right: 0; top: 84px;
    text-align: center; font-size: 13.5px; line-height: 22px; text-transform: uppercase; letter-spacing: -0.4px;
  }
  .stores {
    position: absolute; left: 0; right: 0; top: 164px;
    display: flex; justify-content: center; gap: 16px;
    font-size: 12.5px; font-weight: 600; text-transform: uppercase; letter-spacing: -0.2px;
  }
  .store { display: flex; align-items: center; gap: 5px; }
  .store-square { width: 10px; height: 10px; background: var(--ink); }
  .back-band {
    position: absolute; left: 0; bottom: 0; width: 100%; height: 58px; background: var(--ink);
  }
</style>
</head>
<body>
<main class="canvas">
  <section class="card card--front">
    <header class="front-band">
      <h1 class="choir-name">The Mercy Hill Gospel Choir</h1>
      <p class="church-line">The Harvest Covenant Church of Greenfield - Founded 1792</p>
    </header>
    <div class="contact-block">
      <p class="person">Dean Farrow <span class="person-role">Minister of Music</span></p>
      <div class="contact-grid">
        <span>4827, Marlowe Avenue</span>
        <span class="social"><svg class="social-mark" viewBox="0 0 10 10"><circle cx="5" cy="5" r="4" fill="var(--ink)"/></svg>Picturo mercyhillgc</span>
        <span>Philadelphia, PA 19144</span>
        <span class="social"><svg class="social-mark" viewBox="0 0 10 10"><circle cx="5" cy="5" r="4" fill="var(--ink)"/></svg>Friendwall friendwall.example/mhgc408</span>
        <span>Bookings: (555) 552-MHGC</span>
        <span class="social"><svg class="social-mark" viewBox="0 0 10 10" fill="none" stroke="var(--ink)" stroke-width="1"><circle cx="5" cy="5" r="4.2"/><ellipse cx="5" cy="5" rx="1.8" ry="4.2"/><line x1="0.8" y1="5" x2="9.2" y2="5"/></svg>mercyhillgc.example</span>
      </div>
    </div>
  </section>

  <section class="card card--back">
    <p class="back-message">Music and CD's Recordings<br>Available on Choirs Website<br>and also on</p>
    <div class="stores">
      <span class="store"><span class="store-square"></span>Tunevault</span>
      <span class="store"><span class="store-square"></span>Orbita Music</span>
      <span class="store"><span class="store-square"></span>Disc Pony</span>
    </div>
    <div class="back-band"></div>
  </section>
</main>
</body>
</html>
```